Business Card for Beach theme sports bar called TAVRU

I need a business card designed for our employees, front and back. This will be used by the employees of two business locations to hand out to customers. I've attached the previous business cards we used at one time for a Benwicks (it is now Tavru). Looking for a fresh new card that is elegant but has character.

Target Market(s)

30-60, middle class

Contact Information for Business Card

We are a beach bar and sports bar. I am looking for an elegant business card with the front to have the TAVRU logo. Then on the back I need it to allow a space for employees to write their names and for them to write in their schedule. I have attached our old cards with our old name Benwicks so you can pull everything we need on the cards. one thing is missing is we have another location at 2815 N Willow Crest Rd with a number of 702-418-9351. Since we will use it for both locations it should allow the employee to circle or check mark the bar which they work at.

Font styles to use
Sans Serif

Requirements
Must have
• We are looking for some fresh ideas for the business card. Something that will really stick out to customers when the staff hands them out. Creativity will be looked at positively, but we still want it to look upscale and fun.

```html
<!DOCTYPE html>
<html lang="en">
<head>
<meta charset="utf-8">
<title>Tavru — Employee Business Card</title>
<link href="https://fonts.googleapis.com/css2?family=Roboto+Condensed:wght@400;700&family=Lato:wght@400;700&family=Sacramento&display=swap" rel="stylesheet">
<style>
  :root {
    --bg: #3a3850;
    --gold: #e2c15a;
    --gold-soft: #f1dc86;
    --ink: #1d1c1a;
    --paper: #f7f6f1;
    --box: #d9b94f;
  }
  * { box-sizing: border-box; margin: 0; padding: 0; }
  html, body { width: 1200px; height: 971px; overflow: hidden; }
  body {
    background: var(--bg);
    display: flex;
    flex-direction: column;
    align-items: center;
    justify-content: center;
    gap: 60px;
    font-family: "Lato", sans-serif;
    color: var(--ink);
  }
  .card {
    width: 560px;
    height: 320px;
    border-radius: 4px;
    position: relative;
    overflow: hidden;
  }

  /* Front */
  .card-front {
    background: var(--gold);
    display: flex;
    align-items: center;
    justify-content: center;
    gap: 18px;
  }
  .brand-dot {
    width: 26px; height: 26px;
    border-radius: 50%;
    background: var(--ink);
  }
  .brand-name {
    font-family: "Roboto Condensed", sans-serif;
    font-weight: 700;
    font-size: 82px;
    letter-spacing: 6px;
    color: var(--ink);
  }

  /* Back */
  .card-back {
    background: var(--paper);
    padding: 30px 34px;
  }
  .role-bar {
    display: flex;
    align-items: center;
    height: 54px;
    background: var(--gold);
    border-radius: 27px;
    padding: 7px 7px 7px 24px;
  }
  .role-title {
    font-family: "Roboto Condensed", sans-serif;
    font-weight: 700;
    font-size: 22px;
    letter-spacing: 0.5px;
    margin-right: 20px;
  }
  .name-field {
    flex: 1;
    height: 100%;
    background: var(--paper);
    border-radius: 20px;
    display: flex;
    align-items: center;
    padding-left: 20px;
    font-family: "Sacramento", cursive;
    font-size: 34px;
  }
  .schedule {
    display: flex;
    gap: 12px;
    margin-top: 22px;
  }
  .day {
    display: flex;
    flex-direction: column;
    align-items: center;
    gap: 4px;
    font-family: "Roboto Condensed", sans-serif;
    font-size: 17px;
  }
  .day-box {
    width: 34px; height: 30px;
    border: 2px solid var(--box);
    display: flex; align-items: center; justify-content: center;
  }
  .locations {
    display: flex;
    justify-content: space-between;
    margin-top: 22px;
  }
  .location {
    font-size: 12.5px;
    line-height: 1.35;
    text-align: center;
    width: 46%;
  }
  .location-check {
    display: block;
    margin: 0 auto 6px;
  }
</style>
</head>
<body>

  <section class="card card-front" aria-label="Card front">
    <span class="brand-dot"></span>
    <span class="brand-name">TAVRU</span>
  </section>

  <section class="card card-back" aria-label="Card back">
    <div class="role-bar">
      <span class="role-title">BARTENDER</span>
      <span class="name-field">My Nameiz</span>
    </div>

    <div class="schedule">
      <div class="day">M<span class="day-box"><svg width="22" height="22" viewBox="0 0 22 22"><path d="M3 3 L19 19 M19 3 L3 19" stroke="#1d1c1a" stroke-width="2"/></svg></span></div>
      <div class="day">T<span class="day-box"></span></div>
      <div class="day">W<span class="day-box"></span></div>
      <div class="day">Th<span class="day-box"></span></div>
      <div class="day">F<span class="day-box"></span></div>
      <div class="day">Sa<span class="day-box"></span></div>
      <div class="day">Su<span class="day-box"></span></div>
    </div>

    <div class="locations">
      <div class="location">
        <svg class="location-check" width="18" height="18" viewBox="0 0 18 18"><path d="M2 2 L16 16 M16 2 L2 16" stroke="#d9b94f" stroke-width="1.5"/></svg>
        3160 W Palm Harbor Rd<br>Las Vegas, NV 89146<br>702-530-6274<br>cs@tavrubar.com
      </div>
      <div class="location">
        <svg class="location-check" width="18" height="18" viewBox="0 0 18 18"><path d="M2 2 L16 16 M16 2 L2 16" stroke="#1d1c1a" stroke-width="1.5"/></svg>
        2815 N Willow Crest Rd<br>Las Vegas, NV 89147<br>702-418-9351<br>cs@tavrubar.com
      </div>
    </div>
  </section>

</body>
</html>
```